Life and business Coaching Business Card and Logo

A new design for new company. We coach people to get the best out of themselves in business, life, health , family, career, relationships.
we work in Professional, executive, business and corporate environment. We use art and the processes of making art to work with getting people to delve into and change their mind maps or the way they are currently thinking so that they can move forward towards their goals strategically.
Updates

Project Deadline Extended
Reason: I have been laid up in bed with back problems and have just been able to get back to view designs. several are quiet good and I have given feedback today. I also want to take my project off refundable status as I will choose a design from this brief. regards Rosalind

Target Market(s)

Professional artistic and bold energetic individuals

Industry/Entity Type

Health

Contact Information for Business Card

Hue4Mentoring, Rosalind Pettigrew, Shaping Days Boldly,
Mob:0412958176, Ph: +61 8 93627580,
Professional, Executive, Business and Corporate Coach

Requirements
Must have
• a logo that can be used on all promotional and stationary material.
Should contain a person and be bold/colourful, simple and artistic.
Nice to have
• Room to place qualifications of Business

```html
<!DOCTYPE html>
<html lang="en">
<head>
<meta charset="utf-8">
<title>Hue4Mentoring Business Card</title>
<link rel="stylesheet" href="https://fonts.googleapis.com/css2?family=Arimo:wght@400;700&display=swap">
<style>
  :root {
    --stage-light: #d2d2d2;
    --stage-dark: #8c8c8c;
    --stage-edge: #7a7a7a;
    --card-black: #0d0d0d;
    --zip-blue: #1f8fd8;
    --zip-blue-deep: #1677bd;
    --ink-white: #ffffff;
    --mark-grey: #3c3c3c;
    --tab-dark: #6e6e6e;
    --tab-light: #e2e2e2;
  }
  html, body {
    margin: 0;
    padding: 0;
    overflow: hidden;
  }
  .stage {
    position: relative;
    width: 1200px;
    height: 931px;
    overflow: hidden;
    background: radial-gradient(ellipse at 48% 45%, var(--stage-light) 0%, #b4b4b4 45%, var(--stage-dark) 100%);
    box-shadow: inset 0 0 0 3px var(--stage-edge);
    font-family: "Arimo", Arial, sans-serif;
  }
  .card {
    position: absolute;
    background: var(--card-black);
    overflow: hidden;
    box-shadow: 3px 5px 8px rgba(0, 0, 0, 0.35);
  }
  .card-front { left: 217px; top: 170px; width: 452px; height: 268px; }
  .card-back  { left: 564px; top: 574px; width: 438px; height: 267px; }

  .zip-art {
    position: absolute;
    inset: 0;
    width: 100%;
    height: 100%;
  }
  .brand-mark {
    position: absolute;
    left: 40px;
    top: 62px;
    display: flex;
    align-items: center;
    gap: 6px;
    color: var(--ink-white);
    font-size: 15px;
    font-weight: 700;
    letter-spacing: 0.3px;
  }
  .brand-dot {
    width: 9px;
    height: 9px;
    border-radius: 50%;
    background: var(--ink-white);
  }
  .contact {
    position: absolute;
    left: 30px;
    top: 198px;
    color: var(--ink-white);
    line-height: 17px;
  }
  .contact-name { font-size: 14px; font-weight: 700; letter-spacing: 0.3px; }
  .contact-line { font-size: 14px; font-weight: 400; }

  .back-name {
    position: absolute;
    right: 30px;
    top: 92px;
    color: var(--ink-white);
    font-size: 36px;
    font-weight: 700;
  }
  .back-role {
    position: absolute;
    left: 11px;
    bottom: 13px;
    color: var(--ink-white);
    font-size: 11px;
    font-weight: 700;
    letter-spacing: 0.2px;
  }

  .side-tab {
    position: absolute;
    display: flex;
    align-items: center;
    justify-content: center;
    background: linear-gradient(90deg, var(--tab-dark), var(--tab-light) 55%, #bdbdbd);
  }
  .side-tab span {
    color: var(--ink-white);
    font-size: 32px;
    font-weight: 700;
    letter-spacing: 3px;
    white-space: nowrap;
  }
  .tab-front { left: 1051px; top: 193px; width: 123px; height: 224px; }
  .tab-front span { transform: rotate(-90deg); }
  .tab-back { left: 28px; top: 597px; width: 122px; height: 223px; }
  .tab-back span { transform: rotate(90deg); }

  .crop-marks {
    position: absolute;
    inset: 0;
    width: 1200px;
    height: 931px;
    pointer-events: none;
  }
</style>
</head>
<body>
<main class="stage">

  <svg class="crop-marks" viewBox="0 0 1200 931" aria-hidden="true">
    <g stroke="var(--mark-grey)" stroke-width="1.5" fill="none">
      <path d="M198 146 h12 M198 146 v12"/>
      <path d="M676 146 h-12 M676 146 v12"/>
      <path d="M198 462 h12 M198 462 v-12"/>
      <path d="M676 462 h-12 M676 462 v-12"/>
      <path d="M534 553 h12 M534 553 v12"/>
      <path d="M1025 553 h-12 M1025 553 v12"/>
      <path d="M534 865 h12 M534 865 v-12"/>
      <path d="M1025 865 h-12 M1025 865 v-12"/>
    </g>
  </svg>

  <section class="card card-front" aria-label="Business card front">
    <svg class="zip-art" viewBox="0 0 274 162" preserveAspectRatio="none">
      <defs>
        <linearGradient id="zipTone" x1="0" y1="0" x2="1" y2="1">
          <stop offset="0" stop-color="var(--zip-blue)"/>
          <stop offset="1" stop-color="var(--zip-blue-deep)"/>
        </linearGradient>
      </defs>
      <path role="img" aria-label="Illustration of an opening zip revealing white icons of life, health, family, career and business items"
            d="M90 76 C110 60 135 38 169 27 C200 17 230 10 258 0 L274 0 L274 162 L200 162 C185 150 175 142 169 137 C145 118 118 92 90 76 Z"
            fill="url(#zipTone)"/>
    </svg>
    <div class="brand-mark"><span class="brand-dot"></span>Hue4Mentoring</div>
    <div class="contact">
      <div class="contact-name">ROSALIND PETTIGREW</div>
      <div class="contact-line">Mobile : +412958176</div>
      <div class="contact-line">Phone : +61 8 93627580</div>
    </div>
  </section>

  <section class="card card-back" aria-label="Business card back">
    <div class="back-name">Hue4Mentoring</div>
    <div class="back-role">PROFESSIONAL, EXECUTIVE, BUSINESS AND CORPORATE COACH</div>
  </section>

  <div class="side-tab tab-front"><span>FRONT</span></div>
  <div class="side-tab tab-back"><span>BACK</span></div>

</main>
</body>
</html>
```